Vantrel - corporate Business Card

We need a good look and innovative business card for a new start up company based in Los Angeles called "Vantrel". We are in a payment business, including payment card, app, and ewallet. We are expert in online payment and Card not present (CNP) transaction.
We need an innovative, modern business card.

Our logo font is Aero Matics

Target Market(s)

Startup - Bank - Online Payment - Card Manufacturing

Industry/Entity Type

Startup

Contact Information for Business Card

phone: 555 371 6042 - Address: 4270 Marrowgate blvd, Dunmere Hills, CA 90417

Requirements
Must have
• Message: innovative, professional, expert, high tech, trust, online payment expert, security
Nice to have
• no comment
Should not have
• no Comment

```html
<!DOCTYPE html>
<html lang="en">
<head>
<meta charset="utf-8">
<title>Vantrel – Business Card</title>
<link rel="stylesheet" href="https://fonts.googleapis.com/css2?family=Open+Sans:wght@400;700&display=swap">
<style>
  :root {
    --stage: #bdbdbd;
    --brand-red: #c0172b;
    --brand-red-deep: #a9001a;
    --brand-red-light: #d6253a;
    --paper: #ffffff;
    --blush: #f5e3de;
    --ink-grey: #8a8a8a;
  }
  * { box-sizing: border-box; margin: 0; padding: 0; }
  html, body { width: 1200px; height: 837px; overflow: hidden; }
  body {
    background: var(--stage);
    font-family: "Open Sans", Arial, sans-serif;
    position: relative;
  }
  .card {
    position: absolute;
    top: 270px;
    width: 525px;
    height: 300px;
    overflow: hidden;
    box-shadow: 0 10px 24px rgba(0,0,0,0.18);
  }
  /* Back side */
  .card--back {
    left: 50px;
    background: linear-gradient(120deg, var(--brand-red-deep) 0%, var(--brand-red) 50%, var(--brand-red-light) 100%);
  }
  .card--back .back-circle {
    position: absolute;
    left: -70px; top: 10px;
    width: 280px; height: 280px;
    border-radius: 50%;
    background: rgba(120, 0, 15, 0.18);
  }
  .card--back .wordmark {
    position: absolute;
    left: 150px; top: 112px;
    font-weight: 700;
    font-size: 64px;
    letter-spacing: 1px;
    color: var(--paper);
  }
  /* Front side */
  .card--front {
    left: 625px;
    background: var(--paper);
  }
  .front-circle {
    position: absolute;
    right: -70px; top: 95px;
    width: 260px; height: 260px;
    border-radius: 50%;
    background: var(--blush);
  }
  .contact {
    position: absolute;
    left: 36px; top: 30px;
    color: var(--ink-grey);
    font-size: 13px;
    line-height: 1.35;
  }
  .contact .person-name {
    color: var(--brand-red);
    font-weight: 700;
    font-size: 17px;
    line-height: 1.1;
  }
  .contact .person-role { margin-bottom: 6px; }
  .contact .address { margin-bottom: 6px; }
  .contact .line { display: flex; align-items: center; gap: 7px; }
  .contact .line svg { width: 13px; height: 13px; flex: none; }
  .brand {
    position: absolute;
    left: 36px; top: 200px;
    display: flex;
    align-items: center;
    gap: 10px;
  }
  .brand .brand-dot {
    width: 52px; height: 52px;
    border-radius: 50%;
    background: var(--brand-red);
  }
  .brand .wordmark {
    font-weight: 700;
    font-size: 44px;
    color: var(--brand-red);
    letter-spacing: 1px;
  }
</style>
</head>
<body>
  <section class="card card--back" aria-label="Card back">
    <div class="back-circle"></div>
    <div class="wordmark">vantrel</div>
  </section>

  <section class="card card--front" aria-label="Card front">
    <div class="front-circle"></div>
    <div class="contact">
      <div class="person-name">Dorian Keller</div>
      <div class="person-role">Managing Director</div>
      <div class="address">4270 Marrowgate blvd,<br>Dunmere Hills, CA 90417</div>
      <div class="line">
        <svg viewBox="0 0 14 14" aria-hidden="true"><circle cx="7" cy="7" r="7" fill="var(--brand-red)"/><path d="M4.3 3.6l1.4-.4.8 1.9-.9.7a5 5 0 0 0 2.6 2.6l.7-.9 1.9.8-.4 1.4c-3.4.2-6.3-2.7-6.1-6.1z" fill="#fff"/></svg>
        <span>555 371 6042</span>
      </div>
      <div class="line">
        <svg viewBox="0 0 14 14" aria-hidden="true"><circle cx="7" cy="7" r="7" fill="var(--brand-red)"/><rect x="3.5" y="4.5" width="7" height="5" fill="none" stroke="#fff" stroke-width="1"/><path d="M3.5 4.5L7 7.3l3.5-2.8" fill="none" stroke="#fff" stroke-width="1"/></svg>
        <span>hello@vantrelpay.com</span>
      </div>
    </div>
    <div class="brand">
      <div class="brand-dot"></div>
      <div class="wordmark">vantrel</div>
    </div>
  </section>
</body>
</html>
```